Brand Identity Pack - Communications Services Company

We require our brand identity to be developed further and something we can move across additional brands we are launching. At the moment we have a mixed message around what our businesses brand is and want to concrete this and improve it. We have one element which is like the business card attached and the other which is on our website.

we have a new slogan we want to reiterate across our branding which is;

Consult>Connect>Care

we want to implement this into our logo and website.

areas we want to cover are;

business Cards
Logo update (if you feel the slogan should go in)
Comp slips
Letterhead
A4 Folder
Facebook (look at current)
Twitter (look at current)

We also have a Velmar stride we want to put our brand identity on.

www.tovenzacomms.co.uk is our website.

we are launching Tovenza Payment Services (Card Payment Terminals) of which we have the logo designed and intend to use the same consult>connect>Care as our slogan. This needs to go within our branding.

I have loaded a business card with some of our branding which is slightly confusing and not in line.

help us make our brand super strong :)

Regards
Bram

It Company

```html
<!DOCTYPE html>
<html lang="en">
<head>
<meta charset="utf-8">
<title>Tovenza Payment Services – Business Card</title>
<link href="https://fonts.googleapis.com/css2?family=Arimo:wght@400;700&display=swap" rel="stylesheet">
<style>
  :root {
    --brand-blue: #1a9dd9;
    --ink: #1a1a1a;
    --text-grey: #333333;
    --divider: #c9c9c9;
    --card-white: #ffffff;
    --backdrop: #e9e6e1;
  }
  * { margin: 0; padding: 0; box-sizing: border-box; }
  html, body {
    width: 1071px; height: 1200px; overflow: hidden;
    background: var(--backdrop);
    font-family: "Arimo", Arial, sans-serif;
  }
  .canvas { position: relative; width: 1071px; height: 1200px; }

  .card {
    position: absolute; overflow: hidden; border-radius: 27px;
  }
  .card--front {
    left: 92px; top: 50px; width: 875px; height: 497px;
    background: var(--card-white);
    box-shadow: 0 4px 14px rgba(0,0,0,.18);
  }
  .card--back {
    left: 80px; top: 587px; width: 879px; height: 500px;
    background: var(--brand-blue);
    box-shadow: 0 4px 14px rgba(0,0,0,.18);
  }

  .brand { position: absolute; white-space: nowrap; }
  .brand__name {
    font-weight: 700; line-height: 1;
  }
  .brand__descriptor {
    color: var(--brand-blue); font-size: 27px; letter-spacing: 2.5px; margin-top: 14px;
  }
  .card--front .brand { left: 70px; top: 196px; }
  .card--front .brand__name { color: var(--ink); font-size: 64px; letter-spacing: 2px; }
  .card--back .brand { left: 70px; top: 190px; }
  .card--back .brand__name { color: var(--card-white); font-size: 74px; letter-spacing: 2px; }

  .divider {
    position: absolute; left: 460px; top: 47px; width: 2px; height: 341px;
    background: var(--divider);
  }

  .contact { position: absolute; left: 487px; top: 44px; color: var(--text-grey); }
  .contact__name {
    color: var(--brand-blue); font-weight: 700; font-size: 32px; letter-spacing: .5px;
  }
  .contact__role { font-size: 22px; margin-top: 6px; }
  .contact__list { list-style: none; margin-top: 22px; }
  .contact__item {
    display: flex; align-items: center; gap: 10px;
    font-size: 22px; height: 37px;
  }
  .contact__icon { width: 18px; height: 18px; flex: none; }
  .contact__address { font-size: 22px; line-height: 33px; margin-top: 14px; font-style: normal; }

  .wave { position: absolute; left: 0; bottom: 0; width: 875px; height: 120px; }
  .website {
    position: absolute; right: 80px; bottom: 8px;
    color: var(--card-white); font-size: 23px; letter-spacing: 1px;
  }

  .slogan { position: absolute; left: 0; top: 0; list-style: none; color: var(--card-white); }
  .slogan__item {
    position: absolute; white-space: nowrap;
    font-weight: 700; font-size: 50px; letter-spacing: 1px;
  }
  .slogan__item::before { content: "• "; }
  .slogan__item--consult { left: 505px; top: 120px; }
  .slogan__item--connect { left: 519px; top: 226px; }
  .slogan__item--care    { left: 519px; top: 331px; }
</style>
</head>
<body>
<main class="canvas">

  <section class="card card--front" aria-label="Business card front">
    <div class="brand">
      <div class="brand__name">TOVENZA</div>
      <div class="brand__descriptor">payment services</div>
    </div>

    <div class="divider"></div>

    <div class="contact">
      <h1 class="contact__name">BRAM HALLOWAY</h1>
      <p class="contact__role">Managing Director</p>
      <ul class="contact__list">
        <li class="contact__item">
          <svg class="contact__icon" viewBox="0 0 18 18" aria-hidden="true"><rect x="5" y="1" width="8" height="16" rx="1.5" fill="var(--brand-blue)"/><rect x="6.5" y="3" width="5" height="6" fill="#fff"/></svg>
          07700 318 452
        </li>
        <li class="contact__item">
          <svg class="contact__icon" viewBox="0 0 18 18" aria-hidden="true"><circle cx="9" cy="9" r="8" fill="none" stroke="var(--brand-blue)" stroke-width="1.5"/><path d="M6 5c-1 2 1 7 6 8l1-2-2-1-1 1c-1-.5-2.5-2-3-3l1-1-1-2z" fill="var(--brand-blue)"/></svg>
          01632 604 218
        </li>
        <li class="contact__item">
          <svg class="contact__icon" viewBox="0 0 18 18" aria-hidden="true"><rect x="5" y="2" width="8" height="5" fill="var(--brand-blue)"/><rect x="1" y="7" width="16" height="7" rx="2" fill="var(--brand-blue)"/><rect x="4" y="12" width="10" height="4" fill="var(--brand-blue)"/></svg>
          01632 604 219
        </li>
        <li class="contact__item">
          <svg class="contact__icon" viewBox="0 0 18 18" aria-hidden="true"><rect x="1" y="4" width="16" height="11" rx="1.5" fill="var(--brand-blue)"/><path d="M1.5 5l7.5 5 7.5-5" fill="none" stroke="#fff" stroke-width="1.4"/></svg>
          bram@tovenzacomms.co.uk
        </li>
      </ul>
      <address class="contact__address">
        14 Marlow Business Park<br>
        Ashby Road, Fenmoor<br>
        Kelbridge, KB4 2LT
      </address>
    </div>

    <svg class="wave" viewBox="0 0 875 120" preserveAspectRatio="none" aria-hidden="true">
      <path d="M0 0 C140 40 300 75 470 62 C640 48 780 38 875 45 L875 120 L0 120 Z" fill="var(--ink)"/>
      <path d="M0 50 C200 92 390 82 560 60 C700 44 800 48 875 54 L875 120 L0 120 Z" fill="var(--brand-blue)"/>
    </svg>
    <div class="website">www.tovenzacomms.co.uk</div>
  </section>

  <section class="card card--back" aria-label="Business card back">
    <div class="brand">
      <div class="brand__name">TOVENZA</div>
    </div>
    <ul class="slogan">
      <li class="slogan__item slogan__item--consult">CONSULT</li>
      <li class="slogan__item slogan__item--connect">CONNECT</li>
      <li class="slogan__item slogan__item--care">CARE</li>
    </ul>
  </section>

</main>
</body>
</html>
```